Advertisement Design Project

Attached is the information I need in a big color ad

10X11 that will go in a weekly local paper.
I am open to color and graphics-no pictures of people please.

My logo is also attached, which I would like in the ad.

Sorry for the short notice-I just got a deal on the space and it is due Friday.

```html
<!DOCTYPE html>
<html lang="en">
<head>
<meta charset="utf-8">
<title>Trusts, New Tax Laws – Estate Planning Workshop</title>
<link href="https://fonts.googleapis.com/css2?family=Anton&family=Arimo:ital,wght@0,400;0,700;1,400;1,700&display=swap" rel="stylesheet">
<style>
  :root {
    --gold: #f9b52a;
    --gold-pale: #fde3a6;
    --ink: #2b2b2b;
    --slate: #4a4a4a;
    --frame: #bdbdbd;
    --white: #ffffff;
  }
  * { box-sizing: border-box; margin: 0; padding: 0; }
  html, body { width: 1091px; height: 1200px; overflow: hidden; background: var(--white); }
  .ad {
    position: relative; width: 1091px; height: 1200px;
    border: 1px solid var(--frame);
    font-family: "Arimo", Arial, sans-serif; color: var(--ink);
  }
  .headline {
    position: absolute; left: 0; right: 0; top: 38px; text-align: center;
    font-family: "Anton", Impact, sans-serif; color: var(--gold);
    font-size: 88px; line-height: 1; letter-spacing: 0.5px;
  }
  .subhead {
    position: absolute; left: 0; right: 0; top: 140px; text-align: center;
    font-family: "Anton", Impact, sans-serif; color: var(--slate);
    font-size: 64px; line-height: 1;
  }
  .hero {
    position: absolute; left: 170px; top: 230px; width: 790px; height: 335px;
    background: radial-gradient(ellipse at 45% 55%, #d9b27a 0%, #e9d8bb 28%, #f3eee6 55%, #ffffff 80%);
  }
  .intro {
    position: absolute; left: 66px; top: 582px;
    font-style: italic; font-weight: 700; color: var(--slate); font-size: 36px;
  }
  .questions {
    position: absolute; left: 66px; top: 640px; list-style: none;
  }
  .questions li {
    position: relative; padding-left: 34px; height: 34.6px;
    font-style: italic; font-weight: 700; font-size: 19px; line-height: 26px;
  }
  .questions li::before {
    content: ""; position: absolute; left: 0; top: 5px;
    width: 17px; height: 17px; border-radius: 50%; background: var(--gold);
  }
  .details { position: absolute; left: 610px; top: 638px; font-size: 19.5px; }
  .details .label { color: var(--gold); font-style: italic; font-weight: 700; font-size: 22px; line-height: 36px; }
  .details .presenter { font-style: italic; font-weight: 700; font-size: 22px; line-height: 36px; }
  .details p { line-height: 36px; }
  .details .label.workshop { margin-top: 14px; }
  .values {
    position: absolute; left: 608px; top: 1031px; width: 412px; height: 32px;
    border-radius: 16px; background: var(--gold-pale);
    display: flex; align-items: center; justify-content: center; gap: 14px;
    font-style: italic; font-weight: 700; font-size: 22px;
  }
  .values .dot { width: 13px; height: 13px; border-radius: 50%; background: var(--gold); }
  .footer-band {
    position: absolute; left: 7px; right: 4px; top: 1098px; height: 92px; background: var(--gold);
  }
  .tagline {
    position: absolute; left: 58px; top: 1113px;
    font-style: italic; font-weight: 700; font-size: 18px; line-height: 26px;
  }
  .reserve {
    position: absolute; left: 730px; top: 1111px; font-size: 21px; line-height: 29px;
  }
  .reserve .phone { font-style: italic; font-weight: 700; font-size: 25px; }
  .brand {
    position: absolute; left: 483px; top: 1058px; width: 124px; height: 124px;
    border-radius: 50%; background: var(--white);
    display: flex; align-items: center; justify-content: center; text-align: center;
    font-weight: 700; font-size: 18px; line-height: 20px; color: var(--gold);
  }
</style>
</head>
<body>
<div class="ad">
  <h1 class="headline">Trusts, New Tax Laws</h1>
  <h2 class="subhead">Annuities and Long Term Care</h2>
  <div class="hero" role="img" aria-label="Glass jar of coins resting on banknotes beside a small model house and keys"></div>

  <p class="intro">Come learn what you need to know</p>
  <ul class="questions">
    <li>&nbsp;Is a living trust right for me?</li>
    <li>Does my existing Trust need to be changed?</li>
    <li>Why does Joint Tenancy create tax problems?</li>
    <li>I have a will, isn't that enough?</li>
    <li>Why do I need powers of attorney?</li>
    <li>How much are inheritance taxes?</li>
    <li>What are the new Affordable Care Act taxes?</li>
    <li>How does Long Term Care insurance work?</li>
    <li>How does Long Term Care insurance work?</li>
    <li>how do I plan for those costs?</li>
    <li>The truth about annuites-</li>
    <li>What are the biggest mistakes in estate planning?</li>
  </ul>

  <div class="details">
    <p class="label">Presented by:</p>
    <p class="presenter">marla quinn ellison</p>
    <p class="presenter">Attorney at Law</p>
    <p>1420 Harbor Lane, Cedar Grove.</p>
    <p>Helping&nbsp; Families plan their estates for over 20 years.</p>
    <p class="label workshop">Workshop</p>
    <p>on September 19, 2013</p>
    <p>at 1-2:30pm &amp;&nbsp; 6-7:30pm</p>
    <p>Venue : Bayside Garden Inn Linden</p>
    <p>2250 Meadow Crest Court, Linden, California 95010</p>
  </div>

  <div class="values"><span>Trust</span><span class="dot"></span><span>Relationship</span><span class="dot"></span><span>Integrity</span></div>

  <div class="footer-band"></div>
  <p class="tagline">Security =Good information+Good Planning<br>Be Smart. Plan Ahead.</p>
  <div class="brand">Ellison<br>Law</div>
  <p class="reserve">Seating is limited for a Reservation,<br>Please call: <span class="phone">(555) 014 - 2700</span></p>
</div>
</body>
</html>
```